Stationary design for real estate company in Verana and Tobago

Kestra Realty Ltd. , real estate company operating in Verana and Tobago, requires a sleek, modern and professional stationary package to wow our customers and potential new clients. we want to look sleek and professional; first impressions count in this business!
Business Address:
Level 1, Marlowe Point Tower
4C Seldon Grove Boulevard
Marlowe Point
Colwyn Pereira Highway
Port Halden
Verana
Tel: + 1 555 014 7236
www.kestra-tt.com
info@kestra-tt.com

```html
<!DOCTYPE html>
<html lang="en">
<head>
<meta charset="utf-8">
<title>Kestra Realty Letterhead</title>
<link href="https://fonts.googleapis.com/css2?family=Lato:wght@400;700&display=swap" rel="stylesheet">
<style>
  :root {
    --backdrop: #e9e9ea;
    --paper: #ffffff;
    --navy: #1f3560;
    --gold: #c9a86a;
    --gold-pale: #e6d6b7;
    --ink: #2a2a2a;
    --signature-tone: #ececec;
  }
  * { margin: 0; padding: 0; box-sizing: border-box; }
  html, body { width: 1200px; height: 874px; overflow: hidden; }
  body {
    background: var(--backdrop);
    font-family: "Lato", Arial, sans-serif;
    color: var(--ink);
  }
  .letterhead {
    position: absolute;
    left: 305px; top: 18px;
    width: 590px; height: 838px;
    background: var(--paper);
    box-shadow: 0 2px 10px rgba(0,0,0,.12);
    overflow: hidden;
  }
  .brand {
    position: absolute; left: 44px; top: 92px;
    display: flex; align-items: center; gap: 10px;
  }
  .brand-dot {
    width: 34px; height: 34px; border-radius: 50%;
    background: var(--gold);
  }
  .brand-name {
    font-size: 26px; font-weight: 400; letter-spacing: 3px;
    color: var(--navy); text-transform: uppercase;
  }
  .contact {
    position: absolute; left: 330px; top: 40px;
    padding-left: 14px;
    border-left: 1px solid var(--navy);
    font-size: 8.5px; line-height: 1.35; color: var(--navy);
    font-style: normal;
  }
  .contact-row { display: flex; align-items: center; gap: 5px; }
  .contact-row svg { width: 8px; height: 8px; fill: var(--navy); }
  .contact-address { margin-top: 6px; padding-left: 13px; }
  .letter {
    position: absolute; left: 58px; top: 196px; width: 430px;
    font-size: 10.5px; line-height: 1.45;
  }
  .letter-date { margin-bottom: 14px; }
  .recipient { margin-bottom: 12px; }
  .salutation { font-weight: 700; font-size: 13px; margin-bottom: 12px; }
  .letter p { margin-bottom: 14px; }
  .signoff { margin-top: 22px; }
  .signature {
    margin-top: 20px; width: 180px; height: 46px;
    background: var(--signature-tone); border-radius: 4px;
  }
  .corner-mark {
    position: absolute; right: -170px; top: 340px;
    width: 260px; height: 260px; border-radius: 50%;
    background: var(--gold-pale);
  }
</style>
</head>
<body>
  <main class="letterhead">
    <header>
      <div class="brand">
        <span class="brand-dot"></span>
        <span class="brand-name">Kestra Realty</span>
      </div>
      <address class="contact">
        <div class="contact-row">
          <svg viewBox="0 0 10 10"><path d="M2 0h2l1 3-1.5 1a6 6 0 0 0 2.5 2.5L7 5l3 1v2c0 1-1 2-2 2A8 8 0 0 1 0 2c0-1 1-2 2-2z"/></svg>
          <span>+ 1 555 014 7236</span>
        </div>
        <div class="contact-row">
          <svg viewBox="0 0 10 10"><path d="M0 2h10v6H0zM0 2l5 3.5L10 2v1L5 6.5 0 3z"/></svg>
          <span>info@kestra-tt.com</span>
        </div>
        <div class="contact-row">
          <svg viewBox="0 0 10 10"><circle cx="5" cy="5" r="5"/></svg>
          <span>www.kestra-tt.com</span>
        </div>
        <div class="contact-address">
          Level 1, Marlowe Point Tower<br>
          4C Seldon Grove Boulevard<br>
          Marlowe Point Colwyn Pereira<br>
          Highway Port Halden Verana
        </div>
      </address>
    </header>

    <div class="corner-mark" role="img" aria-label="Large faint brand mark decoration"></div>

    <section class="letter">
      <div class="letter-date">January-03-2020</div>
      <div class="recipient">Mr. Evan Doyle<br>President</div>
      <div class="recipient">Harlow Corporation<br>123 Street Name, Suite# 10<br>City, State, 120023</div>
      <div class="salutation">Dear Mr, Evan</div>
      <p>Lorem ipsum dolor sit amet, consectetur adipiscing elit, sed do eiusmod tempor incididunt ut labore et dolore magna aliqua. Ut enim ad minim veniam, quis nostrud exercitation ullamco laboris nisi ut aliquip ex ea commodo consequat. Duis aute irure dolor in reprehenderit in voluptate velit esse cillum dolore eu fugiat nulla pariatur.</p>
      <p>Lorem ipsum dolor sit amet, consectetur adipiscing elit, sed do eiusmod tempor incididunt ut labore et dolore magna aliqua. Ut enim ad minim veniam, quis nostrud exercitation ullamco laboris nisi ut aliquip ex ea commodo consequat. Duis aute irure dolor in reprehenderit in voluptate velit esse cillum dolore eu fugiat nulla pariatur.</p>
      <p>Lorem ipsum dolor sit amet, consectetur adipiscing elit, sed do eiusmod tempor incididunt ut labore et dolore magna aliqua. Ut enim ad minim veniam, quis nostrud exercitation ullamco laboris nisi ut aliquip ex ea commodo consequat.</p>
      <p>Excepteur sint occaecat cupidatat non proident, sunt in culpa qui officia deserunt mollit anim id est laborum, re et dolore magnam aliquam quaerat voluptatem.</p>
      <div class="signoff">Regards</div>
      <div class="signature" role="img" aria-label="Handwritten signature of Dorian Vale"></div>
    </section>
  </main>
</body>
</html>
```